Marlowbeck Media Stationary

Start up company requires matching stationary templates for Business Cards, letterhead and 'With Compliments' slips. The final design should keep with the style of our kiosk design, investor brochure and other collateral.

```html
<!DOCTYPE html>
<html lang="en">
<head>
<meta charset="utf-8">
<title>Marlowbeck Media Stationery</title>
<link rel="stylesheet" href="https://fonts.googleapis.com/css2?family=Oswald:wght@700&display=swap">
<style>
  :root {
    --brand-blue: #1075bb;
    --band-mid: #6a95d0;
    --band-light: #d0daef;
    --paper: #ffffff;
    --edge-grey: #c9c9c9;
    --mark-square: #7fb2e0;
  }
  * { margin: 0; padding: 0; box-sizing: border-box; }
  html, body { width: 1200px; height: 875px; overflow: hidden; background: var(--paper); }
  .sheet-set { position: relative; width: 1200px; height: 875px; }

  .letterhead, .card-front, .card-back, .compliments-slip {
    position: absolute; overflow: hidden; background: var(--paper);
  }
  .letterhead { left: 70px; top: 55px; width: 528px; height: 748px; border: 1px solid var(--edge-grey); }
  .card-front { left: 641px; top: 158px; width: 237px; height: 154px; border: 1px solid var(--edge-grey); }
  .card-back { left: 914px; top: 158px; width: 237px; height: 154px; background: var(--brand-blue); }
  .compliments-slip { left: 639px; top: 351px; width: 529px; height: 249px; border: 1px solid var(--brand-blue); }

  .header-field {
    position: absolute; left: 0; top: 0; width: 100%;
    background: linear-gradient(to bottom,
      var(--brand-blue) 0%, var(--brand-blue) var(--solid-stop),
      var(--band-mid) calc(var(--solid-stop) + 14%),
      var(--band-light) calc(var(--solid-stop) + 30%),
      var(--paper) 100%);
  }
  .letterhead .header-field { height: 172px; --solid-stop: 42%; }
  .card-front .header-field { height: 126px; --solid-stop: 52%; }
  .compliments-slip .header-field { height: 182px; --solid-stop: 40%; }

  .brand-lockup { position: absolute; display: flex; align-items: center; color: var(--paper);
    font-family: "Oswald", "Arial Narrow", sans-serif; font-weight: 700; }
  .brand-square { background: var(--paper); flex: none; }
  .brand-name { display: flex; flex-direction: column; line-height: 1; text-transform: uppercase; }
  .brand-name .line-main { letter-spacing: 0.01em; }
  .brand-name .line-sub { letter-spacing: 0.34em; }

  .letterhead .brand-lockup { left: 257px; top: 38px; gap: 14px; }
  .letterhead .brand-square { width: 34px; height: 34px; }
  .letterhead .line-main { font-size: 30px; }
  .letterhead .line-sub { font-size: 14px; margin-top: 3px; }

  .compliments-slip .brand-lockup { left: 25px; top: 18px; gap: 14px; }
  .compliments-slip .brand-square { width: 30px; height: 30px; }
  .compliments-slip .line-main { font-size: 27px; }
  .compliments-slip .line-sub { font-size: 13px; margin-top: 3px; }

  .card-front .brand-lockup { left: 70px; top: 32px; gap: 7px; }
  .card-front .brand-square { width: 17px; height: 17px; }
  .card-front .line-main { font-size: 14px; }
  .card-front .line-sub { font-size: 7px; margin-top: 1px; }

  .card-back .back-square { position: absolute; left: 93px; top: 52px; width: 50px; height: 50px;
    background: var(--mark-square); border-radius: 4px; }

  .footer-band { position: absolute; left: 0; bottom: 0; width: 100%; height: 43px; }
  .footer-band .band-light { height: 13px; background: var(--band-light); }
  .footer-band .band-blue { height: 30px; background: var(--brand-blue); }
</style>
</head>
<body>
<main class="sheet-set">

  <section class="letterhead" aria-label="Letterhead">
    <div class="header-field" role="img" aria-label="Blue header with layered wave graphic"></div>
    <div class="brand-lockup">
      <span class="brand-square"></span>
      <span class="brand-name"><span class="line-main">Marlowbeck</span><span class="line-sub">Media</span></span>
    </div>
    <div class="footer-band"><div class="band-light"></div><div class="band-blue"></div></div>
  </section>

  <section class="card-front" aria-label="Business card front">
    <div class="header-field" role="img" aria-label="Blue header with layered wave graphic"></div>
    <div class="brand-lockup">
      <span class="brand-square"></span>
      <span class="brand-name"><span class="line-main">Marlowbeck</span><span class="line-sub">Media</span></span>
    </div>
  </section>

  <section class="card-back" aria-label="Business card back">
    <span class="back-square"></span>
  </section>

  <section class="compliments-slip" aria-label="With compliments slip">
    <div class="header-field" role="img" aria-label="Blue header with layered wave graphic"></div>
    <div class="brand-lockup">
      <span class="brand-square"></span>
      <span class="brand-name"><span class="line-main">Marlowbeck</span><span class="line-sub">Media</span></span>
    </div>
  </section>

</main>
</body>
</html>
```